Elegant Vetani Kalo Rhum Label Design-

We are creating a Rum Distillery in the paradise island of Bora Bora which is a beautiful and exclusive honeymoon and tourist destination in the South Pacific. Our Rum label needs to reflect the beauty of Bora Bora and French Polynesia.
We would like to see designs that include the image of Mount Otemanu (* the mountain of Bora Bora) with an overwater bungalow in the image with the lagoon. We would like the label to have a turquoise color theme with either silver, white, or gold as the outline of the images. We are also open to some tropical colors as well that represent this paradise. The image needs to represent high quality class. The bottle will be sold mostly to tourist at a premium price.

On the label it needs to have Vetani Kalo Rhum as the main name-
Subheader- Light Rhum
Sub Sub header- Distilled and Bottled in Bora Bora
It needs to have 40% vol and 70cl on the label

Target Market(s)

American tourists in Bora Bora, French Polynesia

Industry/Entity Type

Rum Distillery

Colors
0094D4
00A9DD
6FCCEA
C7EBF8
E9F6FB
00AB8E
00BBA5
67D7C9
C6EFE9
E9F9F6

Requirements
Must have
• The mountain image of Otemanu and an overwater bungalow which is symbolic of Bora Bora.

```html
<!DOCTYPE html>
<html lang="en">
<head>
<meta charset="UTF-8">
<title>Vetani Kalo Rhum – Light Rhum Label</title>
<link href="https://fonts.googleapis.com/css2?family=Tinos:wght@400;700&family=Mulish:wght@700;800&display=swap" rel="stylesheet">
<style>
  :root {
    --backdrop: #000000;
    --teal: #1a9ca9;
    --teal-deep: #168c98;
    --white: #ffffff;
    --title-white: #f1f3f3;
    --silver-light: #f2f2f2;
    --silver-mid: #c9cacc;
    --silver-dark: #8d8f93;
    --ink: #111111;
    --silver-gradient: linear-gradient(90deg, var(--silver-light) 0%, #e4e5e6 25%, var(--silver-dark) 55%, #e6e7e8 75%, var(--silver-light) 100%);
  }
  * { margin: 0; padding: 0; box-sizing: border-box; }
  html, body {
    width: 1200px; height: 1200px; overflow: hidden;
    background: var(--backdrop);
  }
  .canvas { position: relative; width: 1200px; height: 1200px; }

  .label {
    position: absolute; left: 355px; top: 224px;
    width: 520px; height: 719px;
    background: var(--silver-gradient);
  }
  .label__panel {
    position: absolute; left: 13px; top: 13px;
    width: 494px; height: 647px;
    background: var(--teal);
    overflow: hidden;
  }
  .leaf-motif {
    position: absolute; border-radius: 50% 45% 50% 40%;
    background: var(--teal-deep); opacity: 0.7;
  }
  .leaf-motif--upper-left { left: -4px; top: 120px; width: 95px; height: 190px; transform: rotate(-20deg); }
  .leaf-motif--right { left: 425px; top: 155px; width: 80px; height: 140px; transform: rotate(15deg); }
  .leaf-motif--lower-left { left: 30px; top: 430px; width: 175px; height: 185px; transform: rotate(-25deg); }

  .brand-name {
    position: absolute; left: 0; top: 18px; width: 100%;
    text-align: center;
    font-family: "Tinos", "Times New Roman", serif;
    font-weight: 400; font-size: 46px; line-height: 46px;
    color: var(--title-white); letter-spacing: 0.5px;
  }

  .scene-frame { position: absolute; left: 96px; top: 122px; }

  .spec {
    position: absolute; top: 538px;
    font-family: "Mulish", Arial, sans-serif;
    font-weight: 800; font-size: 15px; letter-spacing: 2.5px;
    color: var(--white);
  }
  .spec--abv { left: 57px; }
  .spec--volume { left: 386px; }

  .variety-plate {
    position: absolute; left: 85px; top: 565px;
    width: 323px; height: 70px;
    background: var(--silver-gradient);
    padding: 5px 7px;
  }
  .variety-plate__inner {
    width: 100%; height: 100%;
    background: linear-gradient(90deg, #e0e1e2, #d3d4d6 60%, #d9dadb);
    display: flex; align-items: center; justify-content: center;
    font-family: "Tinos", "Times New Roman", serif;
    font-size: 37px; color: var(--teal); padding-top: 3px;
  }

  .origin-band {
    position: absolute; left: 13px; top: 660px;
    width: 494px; height: 26px;
    display: flex; align-items: center; justify-content: center;
    font-family: "Mulish", Arial, sans-serif;
    font-weight: 800; font-size: 13px; letter-spacing: 3.2px;
    color: var(--ink);
  }
  .label__footer-strip {
    position: absolute; left: 13px; top: 686px;
    width: 494px; height: 18px;
    background: var(--teal);
  }
</style>
</head>
<body>
<main class="canvas">
  <section class="label">
    <div class="label__panel">
      <div class="leaf-motif leaf-motif--upper-left" role="img" aria-label="Faint tropical monstera leaf motif"></div>
      <div class="leaf-motif leaf-motif--right" role="img" aria-label="Faint tropical monstera leaf motif"></div>
      <div class="leaf-motif leaf-motif--lower-left" role="img" aria-label="Faint tropical monstera leaf motif"></div>

      <h1 class="brand-name">VETANI KALO<br>RHUM</h1>

      <svg class="scene-frame" width="302" height="434" viewBox="0 0 302 434">
        <defs>
          <linearGradient id="ringSilver" x1="0" y1="0" x2="1" y2="0">
            <stop offset="0" stop-color="#f4f4f4"/>
            <stop offset="0.3" stop-color="#dcdddf"/>
            <stop offset="0.55" stop-color="#8e9094"/>
            <stop offset="0.8" stop-color="#e3e4e5"/>
            <stop offset="1" stop-color="#f4f4f4"/>
          </linearGradient>
          <linearGradient id="lagoonTones" x1="0" y1="0" x2="0" y2="1">
            <stop offset="0" stop-color="#2f7fc4"/>
            <stop offset="0.28" stop-color="#5f8a6f"/>
            <stop offset="0.4" stop-color="#1c6f9a"/>
            <stop offset="0.55" stop-color="#19bfd0"/>
            <stop offset="1" stop-color="#14a9bc"/>
          </linearGradient>
        </defs>
        <ellipse cx="151" cy="217" rx="151" ry="216" fill="url(#ringSilver)"/>
        <ellipse cx="151" cy="217" rx="141" ry="191" fill="url(#lagoonTones)"
                 role="img" aria-label="Mount Otemanu above a turquoise lagoon with an overwater bungalow"/>
      </svg>

      <span class="spec spec--abv">40% VOL</span>
      <span class="spec spec--volume">70CL</span>

      <div class="variety-plate">
        <div class="variety-plate__inner">LIGHT RHUM</div>
      </div>
    </div>

    <p class="origin-band">DISTILLED AND BOTTLED IN BORA BORA</p>
    <div class="label__footer-strip"></div>
  </section>
</main>
</body>
</html>
```